4 'Thank you' greetings cards designs

We are a small greetings card publisher and we need designs for a range of 'Thank you' greetings cards and notecards.
This project is for a total of 4 designs.
Please take a look at this board on Moodpinly, to see the kind of thing we are looking for: https://www.moodpinly.example/dorvek481/thank-you-cards/
The cards will be printed at a maximum size of 131mm x 183mm (including a 3mm bleed) so please provide 300dpi CMYK files at this size. Please ensure that any text (or elements of the design that are not part of the bleed) are at least 11mm in from each edge. Also, please note that cards do not have to have a bleed if your design doesn't require it (e.g. a plain white background).
Please provide 2 designs in 'portrait' orientation and 2 in 'landscape'.
Please provide 2 designs that just have the words 'Thank you' and then 2 designs that include your choice of these alternative messages:
Thank you so much
Thanks very much
Thank you very much
Thanks a million
Just to say thank you
A big thank you
A really big thank you
Feel free to use an exclamation mark on a couple of your designs, if you wish!
Other than the above guidelines, everything else is up to you in terms of colours, fonts, shapes, etc. - but please use the Moodpinly board to see the kind of designs we are looking for.
Thank you!

```html
<!DOCTYPE html>
<html lang="en">
<head>
<meta charset="utf-8">
<title>Thank you card range</title>
<link rel="stylesheet" href="https://fonts.googleapis.com/css2?family=Cookie&display=swap">
<style>
  :root {
    --backdrop: #4dd4cf;
    --card: #ffffff;
    --ink: #111111;
    --wash-strong: rgba(226, 160, 204, 0.60);
    --wash-mid: rgba(230, 172, 210, 0.42);
    --wash-soft: rgba(236, 188, 218, 0.40);
    --wash-clear: rgba(255, 255, 255, 0);
  }
  html, body {
    margin: 0;
    padding: 0;
    overflow: hidden;
  }
  .canvas {
    position: relative;
    width: 1200px;
    height: 1151px;
    background: var(--backdrop);
    overflow: hidden;
  }
  .card {
    position: absolute;
    background: var(--card);
    overflow: hidden;
  }
  .card--landscape-a { left: 29px;  top: 54px;  width: 585px; height: 418px; }
  .card--portrait-a  { left: 638px; top: 9px;   width: 448px; height: 626px; }
  .card--portrait-b  { left: 94px;  top: 501px; width: 460px; height: 642px; }
  .card--landscape-b { left: 592px; top: 678px; width: 578px; height: 414px; }

  .wash {
    position: absolute;
    border-radius: 46% 54% 42% 58% / 55% 44% 56% 45%;
    background: radial-gradient(ellipse at center,
      var(--wash-strong) 0%,
      var(--wash-mid) 58%,
      var(--wash-clear) 80%);
  }
  .wash--corner {
    border-radius: 40% 60% 55% 45% / 50% 40% 60% 50%;
    background: radial-gradient(ellipse at center,
      var(--wash-soft) 0%,
      var(--wash-soft) 55%,
      var(--wash-clear) 82%);
  }
  .wash--streak {
    border-radius: 30%;
    transform: rotate(20deg);
    background: linear-gradient(90deg,
      var(--wash-clear) 0%,
      var(--wash-strong) 55%,
      var(--wash-mid) 100%);
  }
  .wreath {
    position: absolute;
    overflow: visible;
  }
  .wreath circle {
    fill: none;
    stroke: var(--ink);
    stroke-width: 1.3;
  }
  .greeting {
    position: absolute;
    margin: 0;
    transform: translate(-50%, -50%);
    font-family: "Cookie", cursive;
    font-weight: 400;
    color: var(--ink);
    text-align: center;
    white-space: nowrap;
    line-height: 0.88;
  }
</style>
</head>
<body>
<main class="canvas">

  <section class="card card--landscape-a" aria-label="Landscape card: Thank you">
    <div class="wash wash--corner" role="img" aria-label="Soft pink watercolour wash" style="left:-140px; top:-120px; width:440px; height:460px;"></div>
    <div class="wash wash--streak" role="img" aria-label="Pink brush streak" style="left:520px; top:-20px; width:90px; height:220px;"></div>
    <div class="wash" role="img" aria-label="Pink watercolour splash behind the message" style="left:140px; top:60px; width:340px; height:330px;"></div>
    <svg class="wreath" width="312" height="312" style="left:141px; top:44px;" aria-hidden="true">
      <circle cx="156" cy="156" r="154"/>
    </svg>
    <p class="greeting" style="left:297px; top:206px; font-size:80px;">Thank you</p>
  </section>

  <section class="card card--portrait-a" aria-label="Portrait card: Thank you">
    <div class="wash wash--corner" role="img" aria-label="Soft pink watercolour wash" style="left:-120px; top:-160px; width:440px; height:380px;"></div>
    <div class="wash" role="img" aria-label="Pink watercolour splash behind the message" style="left:-10px; top:150px; width:470px; height:340px;"></div>
    <svg class="wreath" width="328" height="328" style="left:59px; top:109px;" aria-hidden="true">
      <circle cx="164" cy="164" r="162"/>
    </svg>
    <p class="greeting" style="left:223px; top:280px; font-size:84px;">Thank you</p>
  </section>

  <section class="card card--portrait-b" aria-label="Portrait card: A big thank you">
    <div class="wash wash--corner" role="img" aria-label="Soft pink watercolour wash" style="left:-120px; top:-160px; width:450px; height:380px;"></div>
    <div class="wash" role="img" aria-label="Pink watercolour splash behind the message" style="left:0px; top:170px; width:470px; height:340px;"></div>
    <svg class="wreath" width="336" height="336" style="left:61px; top:153px;" aria-hidden="true">
      <circle cx="168" cy="168" r="166"/>
    </svg>
    <p class="greeting" style="left:229px; top:327px; font-size:78px;">A big<br>thank you</p>
  </section>

  <section class="card card--landscape-b" aria-label="Landscape card: A big thank you">
    <div class="wash wash--corner" role="img" aria-label="Soft pink watercolour wash" style="left:-140px; top:-120px; width:440px; height:460px;"></div>
    <div class="wash wash--streak" role="img" aria-label="Pink brush streak" style="left:510px; top:-20px; width:90px; height:220px;"></div>
    <div class="wash" role="img" aria-label="Pink watercolour splash behind the message" style="left:140px; top:60px; width:320px; height:320px;"></div>
    <svg class="wreath" width="304" height="304" style="left:137px; top:54px;" aria-hidden="true">
      <circle cx="152" cy="152" r="150"/>
    </svg>
    <p class="greeting" style="left:289px; top:212px; font-size:70px;">A big<br>thank you</p>
  </section>

</main>
</body>
</html>
```